Business Card Design Project

I require a business card with the following information on them for various different people;
name
m:
f:
e:
I have a logo already and will attached that. We are in the construction industry. I require something clean and simple but eye catching at the same time. You can use another colour with our logo if you like and you can style the logo as well if you wish. I am open.
Also it needs to be front and back design.
Industry/Entity Type
Construction
Requirements
Must have
- Logo, name, mobile, fax and email address.
Front and back design

```html
<!DOCTYPE html>
<html lang="en">
<head>
<meta charset="utf-8">
<title>Stoneway Builders — Business Cards</title>
<link rel="stylesheet" href="https://fonts.googleapis.com/css2?family=Quicksand:wght@400&display=swap">
<style>
  :root {
    --canvas: #ffffff;
    --card: #ffffff;
    --band: #323232;
    --edge: #2a2a2a;
    --brand-green: #2fae4a;
    --ink: #454545;
  }
  html, body {
    margin: 0;
    padding: 0;
    width: 1200px;
    height: 900px;
    overflow: hidden;
    background: var(--canvas);
  }
  .sheet {
    position: relative;
    width: 1200px;
    height: 900px;
    font-family: "Quicksand", sans-serif;
  }
  .card {
    position: absolute;
    left: 280px;
    width: 640px;
    height: 366px;
    background: var(--card);
    box-shadow: 0 0 0 1px var(--edge);
    overflow: hidden;
  }
  .card--front { top: 64px; }
  .card--back { top: 470px; }
  .card svg {
    display: block;
    width: 640px;
    height: 366px;
  }
  .band { fill: var(--band); }
  .brand-name {
    fill: var(--ink);
    font-family: "Quicksand", sans-serif;
    font-weight: 400;
    font-size: 64px;
    letter-spacing: 0.5px;
  }
  .contact-name {
    fill: var(--brand-green);
    font-family: "Quicksand", sans-serif;
    font-size: 28px;
  }
  .contact-line {
    fill: var(--brand-green);
    font-family: "Quicksand", sans-serif;
    font-size: 23px;
    letter-spacing: 0.5px;
  }
</style>
</head>
<body>
<main class="sheet">
  <section class="card card--front" aria-label="Card front">
    <svg viewBox="0 0 640 366" xmlns="http://www.w3.org/2000/svg">
      <polygon class="band band--top" points="0,0 640,0 640,32 0,86"/>
      <polygon class="band band--bottom" points="0,346 640,286 640,366 0,366"/>
      <text class="brand-name" x="320" y="188" text-anchor="middle" transform="rotate(-5 320 170)">Stoneway Builders</text>
    </svg>
  </section>

  <section class="card card--back" aria-label="Card back">
    <svg viewBox="0 0 640 366" xmlns="http://www.w3.org/2000/svg">
      <polygon class="band band--top" points="0,0 640,0 640,66 0,20"/>
      <polygon class="band band--bottom" points="0,286 640,350 640,366 0,366"/>
      <g class="contact" transform="rotate(4 320 185)" text-anchor="middle">
        <text class="contact-name" x="320" y="128">Name Name</text>
        <text class="contact-line" x="320" y="168">m:&#160; 214.660.3081</text>
        <text class="contact-line" x="320" y="204">f:&#160; 214.660.3092</text>
        <text class="contact-line" x="320" y="244">e:&#160; info@stonewaybuild.com</text>
      </g>
    </svg>
  </section>
</main>
</body>
</html>
```